Webdesign für freiberuflichen Statiker
Zielgruppe
Ich bin seit 2021 freiberuflicher Statiker. Ich arbeite mit anderen Freelancern / Partnern / Firmen zusammen und lasse von ihnen z.B. Pläne zeichnen. Meine aktuelle Website habe ich selbst designed, mit Wordpress. Diese soll nun aber komplett neu gestaltet werden. Meine Domain www.vendrik-statik.de möchte ich möglichst behalten.
Meine Zielgruppe sind Architekturbüros, Bauträger, private und öffentliche Bauherren. Sie sollen vor allem einen visuellen Eindruck von unserer Arbeit bekommen - durch Fotos (und einem Video auf der Startseite) von Baustellen, von unseren 3D-Modellen oder Berechnungsmodellen.
Aufgabenstellung
Es gibt bereits ein neues Logo. Dieses werde ich mit anhängen. Außerdem habe ich eine pdf-Datei vorbereitet ('SBV_Inhalte Website'), die den groben Aufbau der Website vorgibt und der die Texte entnommen werden können. Auf der ersten Seite des Dokuments stehen außerdem 3 Beispiel-Websites, die ich gut finde und an denen Ihr euch orientieren könnt. Die Farbwahl kann sehr schlicht gehalten werden - ähnlich wie bei den 3 Beispiel-Seiten. Ich liefere eigene Bilder mit, für projektunabhängige Inhalte können aber auch andere Bilder verwendet werden.

```html
<!DOCTYPE html>
<html lang="de">
<head>
<meta charset="utf-8">
<title>SBV – Neubau Hotel Orion</title>
<link rel="stylesheet" href="https://fonts.googleapis.com/css2?family=Inter:wght@400;500;600;700;800&display=swap">
<style>
  :root {
    --ink: #000000;
    --muted: #8c8c8c;
    --paper: #ffffff;
    --footer: #000000;
    --footer-ink: #ffffff;
    --photo-a: #b9b6b2;
    --photo-b: #8e8c88;
    --plan-a: #f4f4f4;
    --plan-b: #dcdcdc;
  }
  * { margin: 0; padding: 0; box-sizing: border-box; }
  html, body { width: 995px; height: 1200px; overflow: hidden; background: var(--paper); }
  body { position: relative; font-family: "Inter", Helvetica, Arial, sans-serif; color: var(--ink); }

  .brand { position: absolute; left: 39px; top: 12px; font-size: 34px; font-weight: 800; letter-spacing: -1px; display: flex; align-items: center; gap: 8px; }
  .brand-dot { width: 10px; height: 10px; background: var(--ink); border-radius: 50%; }

  .main-nav { position: absolute; top: 30px; left: 620px; width: 336px; display: flex; justify-content: space-between; }
  .main-nav a { color: var(--muted); text-decoration: none; font-weight: 700; font-size: 15px; letter-spacing: 0.2px; }

  .hero-photo { position: absolute; left: 591px; top: 79px; width: 404px; height: 373px; background: linear-gradient(160deg, #6d6a66 0%, var(--photo-a) 45%, var(--photo-b) 100%); }

  .eyebrow { color: var(--muted); font-weight: 600; font-size: 14.5px; text-transform: uppercase; }
  .project-year { position: absolute; left: 36px; top: 120px; }
  .project-title { position: absolute; left: 36px; top: 142px; font-size: 49px; line-height: 56px; font-weight: 600; letter-spacing: -0.5px; text-transform: uppercase; }

  .project-facts { position: absolute; left: 36px; top: 281px; display: flex; gap: 44px; font-size: 15px; font-weight: 700; text-transform: uppercase; }
  .fact { display: flex; align-items: center; gap: 8px; }
  .fact svg { width: 16px; height: 16px; }

  .section-sub { position: absolute; left: 36px; top: 383px; }
  .section-title { position: absolute; left: 36px; top: 403px; font-size: 29px; font-weight: 700; letter-spacing: -0.2px; }
  .description { position: absolute; left: 36px; top: 457px; width: 440px; height: 372px; overflow: hidden; font-size: 15px; line-height: 23.3px; font-weight: 600; }
  .description p + p { margin-top: 23.3px; }

  .details { position: absolute; left: 629px; top: 488px; width: 340px; }
  .details h3 { font-size: 15px; font-weight: 700; margin-bottom: 20px; }
  .details dl { display: grid; grid-template-columns: 155px 1fr; row-gap: 8px; font-size: 15px; line-height: 23.5px; }
  .details dt { color: var(--muted); font-weight: 500; }
  .details dd { font-weight: 600; }

  .phases { position: absolute; left: 0; top: 867px; width: 995px; display: grid; grid-template-columns: repeat(3, 1fr); }
  .phase h4 { font-size: 15px; font-weight: 700; padding-left: 36px; height: 33px; }
  .phase:nth-child(3) h4 { padding-left: 32px; }
  .phase-media { height: 186px; }
  .phase-plan { background: linear-gradient(180deg, var(--plan-a), var(--plan-b)); border-right: 1px solid #fff; }
  .phase-site { background: linear-gradient(160deg, #7a7772 0%, var(--photo-a) 50%, var(--photo-b) 100%); border-right: 1px solid #fff; }

  .site-footer { position: absolute; left: 0; top: 1160px; width: 995px; height: 40px; background: var(--footer); color: var(--footer-ink); font-size: 11px; }
  .site-footer .copy { position: absolute; left: 37px; top: 14px; }
  .site-footer nav a { position: absolute; top: 13px; color: var(--footer-ink); text-decoration: none; font-size: 11.5px; }
</style>
</head>
<body>
  <div class="brand"><span>SBV</span><span class="brand-dot"></span></div>

  <nav class="main-nav">
    <a href="#">OFFICE</a>
    <a href="#">PROJEKTE</a>
    <a href="#">EXPERTISE</a>
  </nav>

  <div class="hero-photo" role="img" aria-label="Luftaufnahme des eingerüsteten Hotelrohbaus an einer Straßenkreuzung"></div>

  <p class="eyebrow project-year">Baujahr 20XX</p>
  <h1 class="project-title">Neubau Hotel<br>Orion</h1>

  <div class="project-facts">
    <span class="fact">
      <svg viewBox="0 0 16 16" fill="none" stroke="currentColor" stroke-width="1.2"><path d="M1 5l4-2 6 2 4-2v9l-4 2-6-2-4 2z"/><path d="M8 9.5s-2-2-2-3.3a2 2 0 014 0C10 7.5 8 9.5 8 9.5z"/></svg>
      Velbert, Deutschland
    </span>
    <span class="fact">
      <svg viewBox="0 0 16 16" fill="none" stroke="currentColor" stroke-width="1.4" stroke-dasharray="3 2"><rect x="1.5" y="1.5" width="13" height="13"/></svg>
      CA. 4600 QM
    </span>
  </div>

  <p class="eyebrow section-sub">Subheadline</p>
  <h2 class="section-title">PROJEKTBESCHREIBUNG</h2>
  <div class="description">
    <p>Lorem ipsum dolor sit amet, consetetur sadipscing elitr, sed diam nonumy eirmod tempor invidunt ut labore et dolore magna aliquyam erat, sed diam voluptua. At vero eos et accusam et justo duo dolores et ea rebum. Stet clita kasd gubergren, no sea takimata sanctus est Lorem ipsum dolor sit amet.</p>
    <p>Lorem ipsum dolor sit amet, consetetur sadipscing elitr, sed diam nonumy eirmod tempor invidunt ut labore et dolore magna aliquyam erat, sed diam voluptua. At vero eos et accusam et justo duo dolores et ea rebum. Stet clita kasd gubergren, no sea takimata sanctus est Lorem ipsum dolor sit amet.</p>
    <p>Lorem ipsum dolor sit amet, consetetur sadipscing elitr, sed diam nonumy eirmod tempor invidunt ut labore et</p>
  </div>

  <section class="details">
    <h3>PROJEKT DETAILS</h3>
    <dl>
      <dt>Standort</dt><dd>Velbert, Deutschland</dd>
      <dt>Jahr</dt><dd>20XX</dd>
      <dt>Bauart</dt><dd>Massivbau</dd>
      <dt>Baugrundfläche</dt><dd>ca. 4600 qm</dd>
      <dt>Geschosse</dt><dd>7 Vollgeschosse</dd>
      <dt>Leistung</dt><dd>LP 5</dd>
      <dt>Bauherr</dt><dd>Hotel Nordhang GmbH</dd>
      <dt>Architekt</dt><dd>Brenmark Hotel Concepts</dd>
      <dt>Auftraggeber</dt><dd>Hotel Nordhang GmbH</dd>
    </dl>
  </section>

  <section class="phases">
    <div class="phase">
      <h4>PLANUNG</h4>
      <div class="phase-media phase-plan" role="img" aria-label="Ausführungsplan mit Grundriss und Schnitten"></div>
    </div>
    <div class="phase">
      <h4>UMSETZUNG</h4>
      <div class="phase-media phase-site" role="img" aria-label="Luftaufnahme der Baustelle während der Umsetzung"></div>
    </div>
    <div class="phase">
      <h4>FERTIGSTELLUNG</h4>
      <div class="phase-media phase-site" role="img" aria-label="Luftaufnahme des Gebäudes zur Fertigstellung"></div>
    </div>
  </section>

  <footer class="site-footer">
    <span class="copy">© 2024 studio-falkner.de</span>
    <nav>
      <a href="#" style="left:691px">KONTAKT</a>
      <a href="#" style="left:788px">IMPRESSUM</a>
      <a href="#" style="left:885px">DATENSCHUTZ</a>
    </nav>
  </footer>
</body>
</html>
```